Harborline Kidney Services Brochure - Marketing brochure for a dialysis company in the USA

I want a brochure to be created for my business. I have a brochure that can be used as a comparison. My old Company name is Harborline Kidney Services. The new Company Name is Harborline Kidney Services. I have a sample of the Old Brochure. and I uploaded the Logo of HKS. It will be used by my sales agents to introduce my company to potential client hospitals.

Target Market(s)

CEOs of Acute Hospitals and Medical Centers

Industry/Entity Type

Health Care

Requirements
Must have
• Use the sample as a guide. This project is for a 4 page brochure. (2 letter size pages folded in half crosswise) Use the text from the old brochure to the new brochure, replacing the old info with the new company info as needed.
Nice to have
• Here is my company info:
• Harborline Kidney Services
• 4180 W 61st Ave
• Suite D
• It will be nice if the designer can give me the project files that would allow me to edit the text of the brochure.
• McAllen, TX 78392
• (956) 417-2863
• admin@HarborlineKidneyLLC.example
• www.harborlinekidney.example

```html
<!DOCTYPE html>
<html lang="en">
<head>
<meta charset="utf-8">
<title>Harborline Kidney Services Brochure</title>
<link href="https://fonts.googleapis.com/css2?family=Lato:wght@400;700;900&family=Oswald:wght@400;600&display=swap" rel="stylesheet">
<style>
:root{
  --stage:#1d1d1f;
  --paper:#ffffff;
  --blue:#1f6fc0;
  --blue-deep:#0f4f96;
  --blue-light:#4aa3e6;
  --red:#d9242b;
  --red-deep:#a8121a;
  --ink:#3a3f47;
  --head:#1c5aa5;
  --wash:#e6eff8;
  --photo-a:#b9d3e6;
  --photo-b:#7fa6c4;
}
*{box-sizing:border-box;margin:0;padding:0}
html,body{width:1200px;height:900px;overflow:hidden;background:var(--stage)}
body{position:relative;font-family:"Lato",sans-serif;color:var(--ink)}
.spread{position:absolute;width:510px;height:363px;background:var(--paper);overflow:hidden;box-shadow:0 4px 14px rgba(0,0,0,.6)}
.spread-cover{left:75px;top:62px}
.spread-inside-a{left:643px;top:62px}
.spread-inside-b{left:75px;top:487px}
.spread-inside-c{left:643px;top:487px}
.page{position:absolute;top:0;width:255px;height:100%;overflow:hidden}
.page-left{left:0}
.page-right{left:255px;border-left:1px solid #e4e8ee}
.swoosh{position:absolute;left:0;width:100%;pointer-events:none}
.photo{position:absolute;background:linear-gradient(135deg,var(--photo-a),var(--photo-b))}
.photo-round{border-radius:50%;border:3px solid var(--red)}
.photo-inset{border-radius:10px;border:3px solid var(--red)}
.photo-device{background:linear-gradient(180deg,#f1f4f7,#c9d3dc);border-radius:6px}
.brand{position:absolute;display:flex;align-items:center;gap:4px;font-weight:900;color:var(--blue-deep)}
.brand-dot{width:7px;height:7px;border-radius:50%;background:var(--red)}
.brand-name{line-height:1}
.brand-sub{position:absolute;font-weight:900;color:var(--blue-deep);font-size:6px;letter-spacing:.2px;white-space:nowrap}
.q{position:absolute;font-weight:900;color:var(--head);font-size:6.2px;line-height:1.2}
.q-right{text-align:right}
.txt{position:absolute;font-size:4.6px;line-height:1.35;color:var(--ink)}
.txt p+p{margin-top:3px}
.num-list{position:absolute;list-style:none}
.num-list li{display:flex;gap:6px;font-size:4.8px;line-height:1.35}
.badge{flex:none;width:15px;height:11px;background:var(--blue);color:#fff;font-weight:900;font-size:6.5px;display:flex;align-items:center;justify-content:center}
.contact{position:absolute;color:#fff;font-size:5.2px;line-height:1.4}
.contact-title{font-weight:900;font-size:7.5px;text-decoration:underline;margin-bottom:3px}
.contact b{font-weight:900}
.headline{position:absolute;left:0;width:255px;text-align:center;font-family:"Oswald",sans-serif;color:#fff;line-height:1.1}
.headline .big{display:block;font-size:14.5px;font-weight:600}
.headline .small{display:block;font-size:13px;font-weight:400;letter-spacing:.4px}
.cta{position:absolute;left:36px;top:324px;width:183px;height:18px;border-radius:9px;background:linear-gradient(180deg,#f4f6f8,#cfd6de);display:flex;align-items:center;justify-content:center;font-family:"Oswald",sans-serif;font-weight:600;font-size:11px;color:var(--red)}
.bar-top{position:absolute;left:0;top:0;width:100%;height:9px;background:linear-gradient(90deg,var(--blue-deep),var(--blue),var(--red))}
.bar-bottom{position:absolute;left:0;bottom:0;width:100%;height:9px;background:linear-gradient(90deg,var(--red-deep),var(--red))}
</style>
</head>
<body>

<section class="spread spread-cover">
  <div class="page page-left">
    <div class="photo" style="left:6px;top:8px;width:249px;height:230px" role="img" aria-label="Photo of a nurse caring for a patient in a hospital bed beside a dialysis machine"></div>
    <svg class="swoosh" style="top:0" width="255" height="363" viewBox="0 0 255 363">
      <path d="M0 0 H70 C35 28 12 58 0 90Z" fill="#fff"/>
      <path d="M0 24 C30 9 70 2 120 0 H0Z" fill="var(--red)"/>
      <path d="M0 218 C80 246 170 244 255 222 V363 H0Z" fill="#fff"/>
      <path d="M0 224 C80 252 170 250 255 228 V238 C170 258 80 262 0 236Z" fill="var(--red)"/>
      <defs><linearGradient id="coverBand" x1="0" y1="0" x2="0" y2="1"><stop offset="0" stop-color="#4aa3e6"/><stop offset="1" stop-color="#0f4f96"/></linearGradient></defs>
      <path d="M0 240 C80 264 170 262 255 240 V290 C170 308 80 328 0 345Z" fill="url(#coverBand)"/>
      <path d="M0 345 C80 328 170 308 255 290 V296 C170 314 80 334 0 352Z" fill="var(--red)"/>
      <path d="M0 358 C90 340 180 330 255 328 V332 C180 336 90 346 0 363Z" fill="var(--blue)"/>
    </svg>
    <div class="contact" style="left:18px;top:254px">
      <div class="contact-title">CONTACT US</div>
      <div><b>&#9742; Dial-in Number:</b><br>&nbsp;&nbsp;&nbsp;(956) 417-2863<br><b>&#9742; Fax Number:</b><br>&nbsp;&nbsp;&nbsp;(956) 417-2890</div>
    </div>
    <div class="contact" style="left:108px;top:262px">
      <div><b>email:</b><br>&#9656; admin@HarborlineKidneyLLC.example<br><b>Website:</b><br>&#9656; www.harborlinekidney.example</div>
    </div>
    <div class="brand" style="left:178px;top:306px;font-size:18px"><span class="brand-dot"></span><span class="brand-name">HKS</span></div>
    <div class="brand-sub" style="left:154px;top:326px;font-size:5.5px">HARBORLINE KIDNEY SERVICES</div>
  </div>
  <div class="page page-right">
    <div class="brand" style="left:90px;top:18px;font-size:30px"><span class="brand-dot"></span><span class="brand-name">HKS</span></div>
    <div class="brand-sub" style="left:77px;top:52px">HARBORLINE KIDNEY SERVICES</div>
    <div class="photo" style="left:0;top:68px;width:255px;height:200px" role="img" aria-label="Photo of a smiling nurse tending a patient in a hospital bed"></div>
    <svg class="swoosh" style="top:240px" width="255" height="123" viewBox="0 0 255 123">
      <defs><linearGradient id="coverBandR" x1="0" y1="0" x2="0" y2="1"><stop offset="0" stop-color="#4aa3e6"/><stop offset="1" stop-color="#0f4f96"/></linearGradient></defs>
      <path d="M0 36 C90 6 180 4 255 26 V123 H0Z" fill="url(#coverBandR)"/>
      <path d="M0 32 C90 0 180 -2 255 20 V26 C180 4 90 6 0 38Z" fill="var(--red)"/>
    </svg>
    <div class="headline" style="top:282px"><span class="big">TIRED OF PAYING OUTRAGEOUS</span><span class="small">FOR INPATIENT DIALYSIS ?</span></div>
    <div class="cta">CALL US NOW (956) 417-2863</div>
  </div>
</section>

<section class="spread spread-inside-a">
  <div class="page page-left">
    <svg class="swoosh" style="top:0" width="255" height="40" viewBox="0 0 255 40"><path d="M0 0 H255 V8 C170 2 80 10 0 26Z" fill="var(--wash)"/></svg>
    <div class="q" style="left:14px;top:14px;width:140px">Who is Harborline Kidney Services LLC (HKS) and what services does it provide?</div>
    <div class="txt" style="left:14px;top:34px;width:135px"><p>HKS is the lowest cost, highest quality inpatient dialysis and related services provider in South Texas. HKS has achieved its excellent reputation by offering performance instead of promises.</p><p>Any company can tell you that they provide excellent service. Let us show you truly excellent service instead!</p></div>
    <div class="photo photo-round" style="left:158px;top:10px;width:82px;height:82px" role="img" aria-label="Photo of a hospital dialysis unit"></div>
    <div class="q" style="left:14px;top:122px;width:225px">Our facility currently contracts with another dialysis services provider. Why should we switch to HKS?</div>
    <div class="txt" style="left:14px;top:140px;width:178px"><p>HKS specializes in inpatient dialysis only. Your current provider specializes in outpatient, clinic based dialysis, and sends poorly qualified staff from their clinic to your facility to dialyze your often medically complex and hemodynamically unstable hospitalized patients. Contracting with a company that specializes in outpatient dialysis is similar to hiring a general practitioner to do neurosurgery.</p><p>Inpatient acute dialysis is a specialty, with much sicker and medically unstable clients than an outpatient dialysis clinic, and is best handled by a company that specializes ONLY in inpatient acute dialysis and related inpatient services.</p></div>
    <div class="photo photo-device" style="left:198px;top:140px;width:34px;height:95px" role="img" aria-label="Photo of a dialysis machine"></div>
    <div class="photo photo-inset" style="left:14px;top:245px;width:84px;height:48px" role="img" aria-label="Photo of staff at a patient bedside"></div>
    <div class="q q-right" style="left:104px;top:258px;width:136px">What types of facilities typically contract with HKS?</div>
    <div class="txt" style="left:108px;top:276px;width:132px;text-align:right">All types of inpatient facilities can contract with HKS, including large university medical centers, small community hospitals, long term acute care hospitals, and rehabilitation hospitals.</div>
    <svg class="swoosh" style="top:318px" width="255" height="45" viewBox="0 0 255 45"><path d="M0 10 C90 40 180 42 255 20 V45 H0Z" fill="var(--blue)"/><path d="M0 20 C90 45 180 46 255 30 V36 C180 50 90 50 0 28Z" fill="var(--red)"/></svg>
  </div>
  <div class="page page-right">
    <svg class="swoosh" style="top:0" width="255" height="40" viewBox="0 0 255 40"><path d="M0 0 H255 V30 C170 6 80 2 0 8Z" fill="var(--wash)"/></svg>
    <div class="brand" style="left:24px;top:18px;font-size:18px"><span class="brand-dot"></span><span class="brand-name">HKS</span></div>
    <div class="brand-sub" style="left:14px;top:37px;font-size:5px">HARBORLINE KIDNEY SERVICES</div>
    <ul class="num-list" style="left:8px;top:60px;width:238px">
      <li style="margin-bottom:8px"><span class="badge">07.</span><span>Our contracts are very flexible, so you have the ability to contract for only those services that your facility needs. If you need hemodialysis only, we will tailor your contract to suit your needs. If, in the future, you wish to add other services, a contract addendum can be completed quickly.</span></li>
      <li style="margin-bottom:8px"><span class="badge">08.</span><span>Patient satisfaction is our top priority. If a patient is happy with our inpatient dialysis services, that patient will probably return to your facility when future medical services are needed. Thus, both of us will benefit. We actually do patient satisfaction surveys, and act upon the results.</span></li>
      <li style="margin-bottom:8px"><span class="badge">09.</span><span>We strive to cater to the needs of the nephrologist. We realize that nephrologists are a key driver of hospital inpatient dialysis volume. As such, we seek to cater to their needs.</span></li>
      <li style="margin-bottom:8px"><span class="badge">10.</span><span>Our management is very familiar with the NHAC and SHD survey process, and we provide full support during NHAC and SHD surveys. A member of our top management will be on site during these surveys.</span></li>
      <li style="margin-bottom:8px"><span class="badge">11.</span><span>Any dialysis company can pass a NHAC or SHD inspection when they know a week or two in advance that these surveyors are coming. You need an inpatient dialysis provider that is always ready for inspection without advance notice.</span></li>
      <li><span class="badge">12.</span><span>The HKS education department is very familiar with the NHAC and SHD requirements for staff credentialing and competencies, and strives to ensure that each of our staff members is NHAC and SHD compliant at all times.</span></li>
    </ul>
    <div class="photo photo-inset" style="left:8px;top:284px;width:72px;height:46px" role="img" aria-label="Photo of a clinician at a patient's bedside"></div>
    <div class="q q-right" style="left:92px;top:286px;width:150px">How can I find out more about HKS and its services?</div>
    <div class="txt" style="left:92px;top:302px;width:150px;text-align:right">We're glad you asked! Call us anytime, 24 hours a day, 7 days a week at 1-888-555-0147 extension 2. We will be happy to provide you with a free, no obligations proposal for inpatient dialysis and related services.</div>
    <svg class="swoosh" style="top:337px" width="255" height="26" viewBox="0 0 255 26"><path d="M0 20 C90 2 180 2 255 12 V26 H0Z" fill="var(--blue)"/><path d="M0 16 C90 -1 180 -1 255 8 V12 C180 3 90 3 0 21Z" fill="var(--red)"/></svg>
  </div>
</section>

<section class="spread spread-inside-b">
  <div class="bar-top"></div>
  <div class="page page-left">
    <div class="q" style="left:18px;top:36px;width:230px">How is Harborline Kidney Services LLC different from its competitors?</div>
    <ul class="num-list" style="left:8px;top:60px;width:238px">
      <li style="margin-bottom:10px"><span class="badge">01.</span><span>We are based in South Texas. Our two main competitors are based in distant states. When you have a question or concern, you can contact the president and founder of HKS by mobile phone, 24 hours a day, 7 days a week.</span></li>
      <li style="margin-bottom:10px"><span class="badge">02.</span><span>Acute inpatient dialysis and related services is our ONLY business. We perform these treatments using cutting edge dialysis equipment. Our competitors view their inpatient dialysis programs as "cash cows" that supplement their outpatient clinics, and send their outdated equipment to hospitals.</span></li>
      <li style="margin-bottom:10px"><span class="badge">03.</span><span>We strive to seamlessly integrate with your patient care staff. One of our competitors requires a hospital ICU nurse to stand at the bedside with the dialysis staff member during the entire treatment. Such a practice would never occur with HKS.</span></li>
      <li style="margin-bottom:10px"><span class="badge">04.</span><span>We are committed to being an ethical partner. We realize that finding nurses for hire is sometimes challenging. Therefore, we make it a point not to hire away nurses from the facilities with which we contract.</span></li>
      <li style="margin-bottom:10px"><span class="badge">05.</span><span>We place tremendous power in the hands of our frontline managers. Unlike our competitors, when equipment and other resources are needed, our managers can get what they need quickly.</span></li>
      <li><span class="badge">06.</span><span>We offer more inpatient services more cost effectively than any of our competitors. Our inpatient services include hemodialysis, peritoneal dialysis, continuous venovenous hemodialysis, therapeutic apheresis, PICC line insertion, and hemoperfusion.</span></li>
    </ul>
    <div class="brand" style="left:100px;top:294px;font-size:20px"><span class="brand-dot"></span><span class="brand-name">HKS</span></div>
    <div class="brand-sub" style="left:86px;top:316px">HARBORLINE KIDNEY SERVICES</div>
    <svg class="swoosh" style="top:325px" width="255" height="38" viewBox="0 0 255 38"><path d="M0 20 C90 34 180 30 255 8 V38 H0Z" fill="var(--wash)"/><path d="M0 26 C90 36 180 32 255 12 V16 C180 38 90 40 0 30Z" fill="var(--red)"/></svg>
  </div>
  <div class="page page-right">
    <div class="q" style="left:12px;top:34px;width:200px">How does an acute inpatient dialysis contract work?</div>
    <div class="txt" style="left:12px;top:46px;width:160px"><p>If you decide to contract with us, we provide all the dialysis staff, dialysis specific machines, dialysis water treatment system, dialysis specific supplies, biomedical services, policies and procedures, and credentialing for our staff, all for one flat fee per treatment.</p><p>When the nephrologist writes a treatment order, HKS staff perform that treatment according to the nephrologist's exact specifications. Dialysis treatments can be performed either at the bedside or in a separate dialysis room.</p></div>
    <div class="photo" style="left:178px;top:50px;width:64px;height:38px;background:linear-gradient(135deg,#cfe3f4,#5f9fd6);border-radius:4px" role="img" aria-label="Photo of a dialysis catheter"></div>
    <div class="photo photo-inset" style="left:12px;top:128px;width:78px;height:42px" role="img" aria-label="Photo of a dialysis monitor"></div>
    <div class="q q-right" style="left:96px;top:130px;width:148px">Does HKS have satisfied customers who can provide references?</div>
    <div class="txt" style="left:100px;top:148px;width:108px;text-align:right">Yes. We will be more than happy to provide you with a list of satisfied customers and nephrologists.</div>
    <div class="q" style="left:12px;top:183px;width:170px">Who are HKS's competitors?</div>
    <div class="txt" style="left:12px;top:194px;width:170px"><p>Two large dialysis companies provide most of the chronic outpatient and acute inpatient dialysis in the United States. In many locations, one of these two companies is the only dialysis provider in town, and can charge their hospital clients outrageous prices. The business focus of these two companies is roughly 95% chronic outpatient dialysis and 5% acute inpatient dialysis, so their focus is DEFINITELY NOT inpatient dialysis services.</p><p>Since reimbursement is very meager for chronic outpatient dialysis services, the profitability of a typical dialysis clinic is only about 5% at best. By adding inpatient dialysis to its menu of services, a dialysis outpatient clinic can boost its profitability by several percentage points at your expense.</p></div>
    <div class="photo photo-device" style="left:190px;top:180px;width:46px;height:110px" role="img" aria-label="Photo of a continuous dialysis machine"></div>
    <svg class="swoosh" style="top:325px" width="255" height="38" viewBox="0 0 255 38"><path d="M0 8 C90 30 180 34 255 20 V38 H0Z" fill="var(--wash)"/><path d="M0 12 C90 34 180 36 255 24 V28 C180 40 90 40 0 16Z" fill="var(--red)"/></svg>
  </div>
  <div class="bar-bottom"></div>
</section>

<section class="spread spread-inside-c">
  <div class="bar-top"></div>
  <div class="page page-left">
    <div class="photo" style="left:8px;top:24px;width:46px;height:78px;background:linear-gradient(135deg,#e7eff7,#9bb8d2);border-radius:4px" role="img" aria-label="Photo of a dialyzer filter"></div>
    <div class="q q-right" style="left:70px;top:26px;width:172px">Why are HKS's prices so low in comparison to the competition?</div>
    <div class="txt" style="left:78px;top:42px;width:164px;text-align:right">We do a huge volume of inpatient dialysis treatments, which allows us to purchase large quantities of supplies at lower prices. Unlike our competition, we don't have fifteen layers of management and millions of shareholders to support. In addition, our innovative staff compensation programs, and low turnover help keep our costs low.</div>
    <div class="q q-right" style="left:70px;top:84px;width:172px">Does HKS charge "add-on" fees for after-hours, weekend, callback, or holiday treatments?</div>
    <div class="txt" style="left:78px;top:100px;width:164px;text-align:right">No. We charge one flat fee per inpatient dialysis treatment, regardless of when it is performed.</div>
    <div class="q" style="left:12px;top:132px;width:170px">What are the qualifications of the HKS staff?</div>
    <div class="txt" style="left:12px;top:142px;width:165px">Our staff is experienced in inpatient dialysis and related services. HKS staff are BCLS certified, and can be ACLS certified by our education department on request. All HKS staff receive comprehensive pre-hire drug testing and background checks.</div>
    <div class="photo photo-inset" style="left:184px;top:140px;width:56px;height:96px" role="img" aria-label="Photo of a gloved hand holding a blood sample tube"></div>
    <div class="q" style="left:12px;top:176px;width:165px">Is HKS staff available for STAT, on-call, and after-hours treatments?</div>
    <div class="txt" style="left:12px;top:193px;width:165px">Yes. Part of our commitment to your facility involves being on-call to perform inpatient dialysis treatments 24 hours a day, 7 days a week.</div>
    <div class="q" style="left:12px;top:218px;width:165px">Does HKS employ a biomedical staff to maintain its equipment?</div>
    <div class="txt" style="left:12px;top:235px;width:165px">Yes. We have a full time, fully trained and credentialed biomedical staff. Copies of our machine maintenance and repair records are kept on site at your facility for compliance purposes. Like our dialysis staff, our biomedical staff is available 24 hours a day, 7 days a week.</div>
    <svg class="swoosh" style="top:300px" width="255" height="63" viewBox="0 0 255 63"><path d="M0 20 C90 40 180 40 255 24 V63 H0Z" fill="var(--wash)"/></svg>
  </div>
  <div class="page page-right">
    <div class="q" style="left:10px;top:22px;width:150px">Is HKS insured?</div>
    <div class="txt" style="left:10px;top:31px;width:150px">HKS maintains comprehensive malpractice, workers' compensation, and employee health insurance coverage.</div>
    <div class="photo photo-round" style="left:170px;top:14px;width:72px;height:72px" role="img" aria-label="Photo of dialysis tubing on a machine"></div>
    <div class="q" style="left:10px;top:50px;width:155px">What CQI/QA support does HKS provide?</div>
    <div class="txt" style="left:10px;top:60px;width:155px">We provide monthly inpatient dialysis specific CQI/QA in full collaboration with your infection control department and other departments. We also provide monthly water culture and LAL testing of our equipment, and yearly MDSA testing of our equipment.</div>
    <div class="photo photo-inset" style="left:10px;top:110px;width:54px;height:110px" role="img" aria-label="Photo of a nurse operating an apheresis machine"></div>
    <div class="q" style="left:72px;top:112px;width:170px">Does HKS offer therapeutic apheresis.</div>
    <div class="txt" style="left:72px;top:122px;width:172px"><p>Yes. One of the most exciting new therapies available to treat autoimmune diseases is therapeutic apheresis, and HKS is at the forefront of delivering these specialized treatments. HKS utilizes state of the art equipment to perform cell separation therapy in the treatment of a wide range of diseases. HKS offers therapeutic apheresis on the same 24/7/365 basis as our inpatient dialysis services, including weekends and holidays.</p><p>Other providers not rooted in rapid-response, around-the-clock service tend to prefer normal business hours. Often, our hospital clients' patients need us during other than normal business hours, and we respond accordingly.</p></div>
    <div class="q" style="left:10px;top:244px;width:160px">If our facility agrees to contract with HKS for inpatient dialysis and related services, how quickly can the transition from our current dialysis provider to HKS be completed?</div>
    <div class="txt" style="left:10px;top:282px;width:150px">The transition can occur overnight in many cases. We have a dedicated transition team that takes care of these situations so that your facility never experiences a lapse in inpatient dialysis coverage.</div>
    <div class="photo photo-inset" style="left:174px;top:250px;width:70px;height:58px" role="img" aria-label="Photo of a patient's arm during dialysis"></div>
  </div>
  <div class="bar-bottom"></div>
</section>

</body>
</html>
```